Bref créative
QR cards
Lantern Medical
Simple
Lantern Medical LLC
Cards
817 Hollowbrook Ave
Fernhollow Heights, NJ 07990
Info@lanternmedicalcare.example
www.lanternmedicalcare.example
on the back of card
Has an Appointment
Mon____ At ____
Tue____At____
etc thru Saturday

```html
<!DOCTYPE html>
<html lang="en">
<head>
<meta charset="utf-8">
<title>Lantern Medical – Business Card</title>
<link rel="stylesheet" href="https://fonts.googleapis.com/css2?family=Open+Sans:wght@300;400;600;700&display=swap">
<style>
  :root {
    --bg: #e9e7e4;
    --card: #ffffff;
    --card-fade: #e9eaee;
    --band-dark: #1e2630;
    --band-mid: #3a4552;
    --purple: #5b3f9e;
    --purple-light: #8a6bd1;
    --grey-band: #8c8f94;
    --ink: #333a44;
    --line: #8a8d92;
  }
  * { box-sizing: border-box; margin: 0; padding: 0; }
  html, body { width: 1200px; height: 896px; overflow: hidden; }
  body {
    background: var(--bg);
    font-family: "Open Sans", Arial, sans-serif;
    color: var(--ink);
    position: relative;
  }
  .card {
    position: absolute;
    background: linear-gradient(180deg, var(--card) 0%, var(--card-fade) 100%);
    box-shadow: 0 6px 18px rgba(0,0,0,.18);
    overflow: hidden;
  }

  /* front */
  .card--front { left: 73px; top: 73px; width: 570px; height: 400px; }
  .front__band {
    height: 163px;
    background:
      repeating-linear-gradient(90deg, rgba(255,255,255,.04) 0 3px, rgba(0,0,0,.05) 3px 9px),
      radial-gradient(ellipse at 55% 40%, var(--band-mid) 0%, var(--band-dark) 75%);
    display: flex;
    align-items: center;
    justify-content: center;
    gap: 14px;
    border-bottom: 3px solid #b9bcc2;
  }
  .brand__dot {
    width: 22px; height: 22px; border-radius: 50%;
    background: var(--purple-light);
  }
  .brand__name {
    font-size: 42px;
    font-weight: 300;
    letter-spacing: 1px;
    color: #e6e8ec;
  }
  .front__body {
    position: relative;
    height: 234px;
  }
  .company {
    position: absolute;
    left: 26px; top: 36px;
    font-size: 14px;
    font-weight: 700;
    color: var(--purple);
  }
  .contact {
    position: absolute;
    left: 290px; top: 30px;
    list-style: none; font-size: 13px; line-height: 19px;
  }
  .contact li { display: flex; align-items: flex-start; gap: 7px; white-space: nowrap; }
  .contact svg { width: 13px; height: 13px; margin-top: 3px; flex: none; }
  .contact .indent { padding-left: 20px; }

  /* back */
  .card--back { left: 595px; top: 510px; width: 537px; height: 335px; padding: 24px 26px; }
  .back__title { font-size: 15px; font-weight: 700; margin-bottom: 14px; }
  .field { display: flex; align-items: flex-end; font-size: 12px; margin-bottom: 16px; }
  .field__rule { border-bottom: 1px solid var(--line); height: 1px; margin-left: 10px; margin-bottom: 4px; }
  .days { display: flex; gap: 12px; font-size: 11px; margin: 16px 0 40px; }
  .day { display: flex; align-items: center; gap: 6px; }
  .day__box { width: 20px; height: 20px; border: 1px solid #555; background: #fff; }
  .policy__title { font-size: 12px; font-weight: 700; margin-bottom: 4px; }
  .policy__text { font-size: 11px; }
  .back__band { position: absolute; left: 0; right: 0; bottom: 0; width: 100%; height: 34px; }
</style>
</head>
<body>

<section class="card card--front" aria-label="Business card front">
  <div class="front__band">
    <span class="brand__dot"></span>
    <span class="brand__name">LANTERN MEDICAL</span>
  </div>
  <div class="front__body">
    <p class="company">Lantern Medical LLC</p>
    <ul class="contact">
      <li><svg viewBox="0 0 12 12"><circle cx="6" cy="6" r="6" fill="var(--purple)"/><path d="M3 6.5 6 3.5 9 6.5V9H3Z" fill="#fff"/></svg>817 Hollowbrook Ave</li>
      <li class="indent">Fernhollow Heights, NJ 07990</li>
      <li><svg viewBox="0 0 12 12"><circle cx="6" cy="6" r="6" fill="var(--purple)"/><path d="M4 3h1.5l.5 2-1 .7a4 4 0 0 0 1.3 1.3l.7-1 2 .5V8a1 1 0 0 1-1 1A5 5 0 0 1 3 4a1 1 0 0 1 1-1Z" fill="#fff"/></svg>908-555-0170</li>
      <li><svg viewBox="0 0 12 12"><circle cx="6" cy="6" r="6" fill="var(--purple)"/><rect x="3" y="4" width="6" height="4.5" fill="#fff"/><rect x="4" y="2.5" width="4" height="2" fill="#fff"/></svg>908-555-0106</li>
      <li><svg viewBox="0 0 12 12"><circle cx="6" cy="6" r="6" fill="var(--purple)"/><rect x="3" y="4" width="6" height="4" fill="#fff"/><path d="M3 4 6 6.3 9 4" stroke="var(--purple)" stroke-width=".8" fill="none"/></svg>Info@lanternmedicalcare.example</li>
      <li><svg viewBox="0 0 12 12"><circle cx="6" cy="6" r="6" fill="var(--purple)"/><circle cx="6" cy="6" r="3" fill="none" stroke="#fff" stroke-width=".9"/><path d="M3 6h6M6 3v6" stroke="#fff" stroke-width=".8"/></svg>www.lanternmedicalcare.example</li>
    </ul>
  </div>
</section>

<section class="card card--back" aria-label="Appointment card back">
  <h2 class="back__title">Appointment</h2>
  <div class="field">Name:<span class="field__rule" style="width:400px"></span></div>
  <div class="field">Date:<span class="field__rule" style="width:200px"></span><span style="margin-left:14px">Time:</span><span class="field__rule" style="width:150px"></span></div>
  <div class="days">
    <span class="day"><span class="day__box"></span>MON</span>
    <span class="day"><span class="day__box"></span>TUE</span>
    <span class="day"><span class="day__box"></span>WED</span>
    <span class="day"><span class="day__box"></span>THU</span>
    <span class="day"><span class="day__box"></span>FRI</span>
    <span class="day"><span class="day__box"></span>SAT</span>
  </div>
  <p class="policy__title">Cancellation Policy</p>
  <p class="policy__text">We require 24 hours cancellation for appointments otherwise a charge may be incurred.</p>
  <svg class="back__band" viewBox="0 0 537 34" preserveAspectRatio="none">
    <defs>
      <linearGradient id="band-purple" x1="0" x2="1">
        <stop offset="0" stop-color="#ffffff" stop-opacity="0"/>
        <stop offset=".35" stop-color="#7b5cc8"/>
        <stop offset="1" stop-color="#4a2f8c"/>
      </linearGradient>
    </defs>
    <polygon points="0,20 360,20 340,34 0,34" fill="url(#band-purple)"/>
    <polygon points="375,0 537,0 537,34 345,34" fill="var(--grey-band)"/>
  </svg>
</section>

</body>
</html>
```